Kestrel Plumbing business card full re design & logo design

Kestrel Plumbing is a Sydney based mechanical plumbing contractor company.
We would like a full redesign with new logo etc which we can take to a future website, uniforms, vehicle sign writing etc.
Blue is my preferred choice of colour but i would be open to see a couple of alternatives thrown in the mix to see how they compare. I am open to see on white cards, black cards etc. Open to many new ideas.
Please see attached original business cards which have been used for the last 5 years.

Target Market(s)

Mechanical services industry.

Industry/Entity Type

Plumbing

Contact Information for Business Card

Dale Fenmore
Director

Mob: 0427 596 418
Email: dale@kestrelplumbing-demo.net.au
PO BOX 782
Brookmere NSW 2163
Lic: 518604k

Logo Text

Kestrel Plumbing

Font styles to use
Sans Serif

Colors
0655a3
3276b5
0792cd
33a6d7
85cae6
000000
333333
474747

Requirements
Must have
• Things that make it very professional and very well presented.
Nice to have
• Same description or very similar to attached uploaded file
Should not have
• Anything that makes it look unprofessional or cartoony.

```html
<!DOCTYPE html>
<html lang="en">
<head>
<meta charset="utf-8">
<title>Kestrel Plumbing – Business Card</title>
<link rel="stylesheet" href="https://fonts.googleapis.com/css2?family=Open+Sans:ital,wght@0,400;0,600;0,700;1,400&display=swap">
<style>
  :root {
    --blue-deep: #0655a3;
    --blue-mid: #3276b5;
    --blue-bright: #0792cd;
    --blue-sky: #33a6d7;
    --blue-pale: #85cae6;
    --band-blue: #1f64a1;
    --ink: #333333;
    --ink-soft: #474747;
    --paper: #ffffff;
    --backdrop: #eceae6;
  }
  * { box-sizing: border-box; margin: 0; padding: 0; }
  html, body {
    width: 1200px; height: 1200px; overflow: hidden;
    background: var(--backdrop);
    font-family: "Open Sans", Arial, sans-serif;
  }
  .sheet {
    width: 1200px; height: 1200px;
    display: flex; flex-direction: column; align-items: center; justify-content: center;
    gap: 48px;
  }
  .card {
    position: relative;
    width: 860px; height: 526px;
    overflow: hidden;
    box-shadow: 0 6px 18px rgba(0,0,0,0.12);
  }

  /* Front */
  .card-front { background: var(--paper); }
  .brand {
    position: absolute; left: 300px; top: 62px;
    display: flex; align-items: center; gap: 14px;
  }
  .brand-dot {
    width: 34px; height: 34px; border-radius: 50%;
    background: var(--blue-deep);
  }
  .brand-name {
    font-weight: 700; font-size: 38px; letter-spacing: 3px;
    color: var(--blue-deep); text-transform: uppercase;
  }
  .contact {
    position: absolute; left: 120px; top: 178px;
    color: var(--ink);
  }
  .contact-name {
    font-size: 34px; font-weight: 400; color: var(--blue-deep); line-height: 1.1;
  }
  .contact-role { font-size: 16px; color: var(--ink-soft); margin-bottom: 18px; }
  .contact-lines { font-size: 16px; line-height: 1.45; color: var(--ink); }
  .contact-lines .label { color: var(--blue-mid); font-weight: 600; }
  .service-band {
    position: absolute; left: 0; right: 0; bottom: 0; height: 112px;
    background: var(--band-blue);
    display: flex; align-items: center; padding-left: 64px;
    color: var(--paper); font-size: 24px; letter-spacing: 3px;
    white-space: nowrap;
  }

  /* Back */
  .card-back {
    background: linear-gradient(150deg, var(--blue-bright) 0%, var(--blue-deep) 70%);
    color: var(--paper);
  }
  .back-heading {
    position: absolute; left: 100px; top: 54px;
    font-size: 38px; font-weight: 700; letter-spacing: 1px;
  }
  .specialities {
    position: absolute; left: 430px; top: 140px;
  }
  .specialities-title { font-size: 30px; font-weight: 700; margin-bottom: 10px; }
  .specialities-list { list-style: none; font-size: 25px; font-weight: 600; line-height: 1.45; }
  .specialities-list li::before { content: "•"; margin-right: 14px; }
  .tagline {
    position: absolute; left: 56px; bottom: 52px;
    font-size: 24px; font-style: italic; font-weight: 400;
  }
</style>
</head>
<body>
<main class="sheet">
  <section class="card card-front" aria-label="Business card front">
    <div class="brand">
      <span class="brand-dot"></span>
      <span class="brand-name">Kestrel Plumbing</span>
    </div>
    <div class="contact">
      <p class="contact-name">Dale Fenmore</p>
      <p class="contact-role">Director</p>
      <div class="contact-lines">
        <p><span class="label">Mob:</span> 0427 596 418</p>
        <p><span class="label">Email:</span> dale@kestrelplumbing-demo.net.au</p>
        <p>PO BOX 782</p>
        <p>Brookmere NSW 2163</p>
        <p><span class="label">Lic:</span> 518604k</p>
      </div>
    </div>
    <div class="service-band">MECHANICAL PIPING | CHW | HW | CW | REFRIG</div>
  </section>

  <section class="card card-back" aria-label="Business card back">
    <h2 class="back-heading">MECHANICAL PLUMBING SERVICES</h2>
    <div class="specialities">
      <p class="specialities-title">Specialising in:</p>
      <ul class="specialities-list">
        <li>Make Good</li>
        <li>Refurbishment</li>
        <li>Tenacy Fit Out</li>
        <li>Plant Room Works</li>
        <li>Shut Downs</li>
        <li>Change Overs</li>
      </ul>
    </div>
    <p class="tagline">Kestrel have the SOLUTION</p>
  </section>
</main>
</body>
</html>
```